Real Estate Sign Project

We need a Real Estate sign that promotes the property being listed and our company and agent listing the property. The images need to be able to be swapped out so we can use the template for each listing we have. I have a sample from another company that shows what were are trying to accomplish. Would want ours to be unique using our logo and the colors in our logo. We would like to not have to use a rider. Would want agents name and phone number to be part of the 36" x 24" sign.

Industry/Entity Type

Real Estate

Requirements
Must have
• Sign dimensions are 36 inches by 24 inches (36" across and 24" up down). Use example.of.sign.we.want.jpg as the direction we want to go but with a different layout and our logo and colors. This would be just a template that we can swap out new pictures, address, price, website, agents contact info for each home we are listing. Like the idea of the pictures bleeding off the sides. Please use free stock photos for the home images as we will be changing these out for each listing. Please incorporate all info including agents info into the one sign. File must be layered so we can change the pictures, price, website, agent, etc. We use GIMP (.xcf) file

```html
<!DOCTYPE html>
<html lang="en">
<head>
<meta charset="utf-8">
<title>Harlow – For Sale Sign</title>
<link href="https://fonts.googleapis.com/css2?family=Arimo:wght@700&family=PT+Sans+Narrow:wght@400;700&family=Roboto+Condensed:wght@400&family=Tinos:wght@700&display=swap" rel="stylesheet">
<style>
  :root {
    --orange: #f26a10;
    --orange-light: #f7923a;
    --orange-deep: #e05a08;
    --blue: #1b80d6;
    --navy: #1d4f8f;
    --grey: #8d8d8d;
    --white: #ffffff;
  }
  * { box-sizing: border-box; margin: 0; padding: 0; }
  html, body { width: 1200px; height: 833px; overflow: hidden; background: var(--white); }
  .sign { position: relative; width: 1200px; height: 833px; background: var(--white); }
  .block { position: absolute; }

  .corner-panel { left: 37px; top: 40px; width: 425px; height: 403px; }
  .brand {
    left: 62px; top: 100px; width: 180px;
    display: flex; align-items: center; gap: 10px;
    font-family: "Arimo", sans-serif; font-weight: 700; font-size: 40px;
    color: var(--navy); letter-spacing: -0.5px;
  }
  .brand-dot { width: 22px; height: 22px; border-radius: 50%; background: var(--orange); flex: none; }

  .headline {
    left: 140px; top: 228px; width: 302px; text-align: right;
    font-family: "Arimo", sans-serif; font-weight: 700; font-size: 118px; line-height: 96px;
    color: var(--white); letter-spacing: -3px;
    text-shadow: 2px 3px 4px rgba(0,0,0,0.25);
  }

  .photo { position: absolute; }
  .photo-exterior { left: 455px; top: 40px; width: 465px; height: 395px;
    background:
      radial-gradient(ellipse 70% 45% at 45% 62%, rgba(214,190,150,0.95) 0%, rgba(214,190,150,0) 100%),
      linear-gradient(180deg, #2c5fb6 0%, #4f86d2 22%, #c9b48f 42%, #d8c4a0 70%, #b9a583 86%, #4f8a34 100%); }
  .photo-bath { left: 930px; top: 40px; width: 235px; height: 395px;
    background:
      radial-gradient(ellipse 60% 40% at 30% 35%, rgba(240,220,190,0.8) 0%, rgba(240,220,190,0) 100%),
      linear-gradient(180deg, #e8dccb 0%, #b7804e 35%, #8a4a22 70%, #c7a07a 100%); }
  .photo-kitchen { left: 455px; top: 530px; width: 317px; height: 260px;
    background:
      radial-gradient(ellipse 50% 40% at 55% 75%, rgba(184,104,50,0.85) 0%, rgba(184,104,50,0) 100%),
      linear-gradient(180deg, #e6d2b2 0%, #c78a52 35%, #b9773f 60%, #eae2d2 100%); }
  .photo-living { left: 782px; top: 530px; width: 383px; height: 260px;
    background:
      radial-gradient(ellipse 45% 50% at 30% 35%, rgba(246,240,214,0.9) 0%, rgba(246,240,214,0) 100%),
      linear-gradient(180deg, #efe6c8 0%, #d6c49a 40%, #7d4a2c 75%, #4a2a1a 100%); }

  .info-bar {
    position: absolute; top: 443px; height: 79px; background: var(--blue);
    color: var(--white); display: flex; align-items: center; justify-content: center;
  }
  .price { left: 37px; width: 408px; font-family: "Tinos", serif; font-weight: 700; font-size: 44px; }
  .address { left: 455px; width: 317px; font-family: "Roboto Condensed", sans-serif; font-size: 30px; }
  .features { left: 782px; width: 383px; font-family: "Roboto Condensed", sans-serif; font-size: 21px;
    flex-direction: column; align-items: flex-start; padding-left: 49px; line-height: 29px; }

  .agent-card {
    position: absolute; left: 37px; top: 530px; width: 408px; height: 260px;
    background: var(--grey); color: var(--white);
    font-family: "PT Sans Narrow", sans-serif; text-align: center;
  }
  .agent-name { position: absolute; top: 50px; width: 100%; font-size: 50px; }
  .agent-name strong { font-weight: 700; }
  .agent-name .divider { font-weight: 400; margin: 0 10px; }
  .agent-phone { position: absolute; top: 136px; width: 100%; font-size: 50px; font-weight: 700; }
</style>
</head>
<body>
<main class="sign">
  <svg class="block corner-panel" viewBox="0 0 425 403" aria-hidden="true">
    <defs>
      <linearGradient id="peel" x1="0" y1="0" x2="1" y2="1">
        <stop offset="0" stop-color="var(--orange-light)"/>
        <stop offset="0.5" stop-color="var(--orange)"/>
        <stop offset="1" stop-color="var(--orange-deep)"/>
      </linearGradient>
    </defs>
    <path d="M412 0 L425 0 L418 403 L0 403 L0 398 Q12 386 24 372 L400 14 Q407 6 412 0 Z" fill="url(#peel)"/>
  </svg>

  <div class="block brand"><span class="brand-dot"></span>Harlow</div>
  <h1 class="block headline">For<br>Sale</h1>

  <div class="photo photo-exterior" role="img" aria-label="Photo of the two-storey house front with garage and lawn"></div>
  <div class="photo photo-bath" role="img" aria-label="Photo of the master bathroom with tiled tub"></div>

  <div class="info-bar price">$ 250,000 Only</div>
  <div class="info-bar address">2714 Maple Road</div>
  <div class="info-bar features">
    <span>4 Bedrooms &nbsp;|&nbsp; 3.5 Baths</span>
    <span>3200 Finished SF &nbsp;|&nbsp; 2-Car Garage</span>
  </div>

  <section class="agent-card">
    <p class="agent-name">Agent<span class="divider">|</span><strong>Dale Morgan</strong></p>
    <p class="agent-phone">555/018-2740</p>
  </section>

  <div class="photo photo-kitchen" role="img" aria-label="Photo of the kitchen with wood cabinets and island"></div>
  <div class="photo photo-living" role="img" aria-label="Photo of the living room with tall windows and fireplace"></div>
</main>
</body>
</html>
```